Business Card for Veltrano, a french tech company

Tech company
New technologies
Serious design
Dark theme

User info :
Name: Mathis CORLAVE
Position: Co-Founder & CEO
Tel: (+33) 6 58 24 90 37
Email: mathis@veltrano.io
Website: www.veltrano.io
Address: 17 rue des Tanneurs 69002 LYON

Attached is the business logo file.

```html
<!DOCTYPE html>
<html lang="fr">
<head>
<meta charset="utf-8">
<title>Veltrano — Business Card</title>
<link rel="stylesheet" href="https://fonts.googleapis.com/css2?family=Rubik:wght@400;500;700&display=swap">
<style>
  :root {
    --page-bg: #2b2d30;
    --navy-deep: #0a0f33;
    --navy: #141a4d;
    --navy-ink: #15124a;
    --magenta: #e0189a;
    --violet: #8a3fb0;
    --teal: #0a6f9a;
    --paper: #ffffff;
    --text-dark: #1a1a2e;
    --font-main: "Rubik", sans-serif;
  }
  * { box-sizing: border-box; margin: 0; padding: 0; }
  html, body {
    width: 1200px;
    height: 939px;
    overflow: hidden;
    background: var(--page-bg);
    font-family: var(--font-main);
  }
  .sheet {
    width: 1200px;
    height: 939px;
    display: flex;
    flex-direction: column;
    align-items: center;
    justify-content: center;
    gap: 40px;
  }
  .card {
    width: 700px;
    height: 400px;
    position: relative;
    overflow: hidden;
    box-shadow: 0 12px 30px rgba(0,0,0,0.45);
  }

  /* Front */
  .card--front {
    background: var(--navy-deep);
    display: flex;
    align-items: center;
    justify-content: center;
  }
  .front-texture {
    position: absolute;
    inset: 0;
    background: radial-gradient(ellipse at 60% 40%, #1b2260 0%, var(--navy-deep) 70%);
    opacity: 0.9;
  }
  .front-wordmark {
    position: relative;
    font-size: 84px;
    font-weight: 500;
    letter-spacing: 2px;
    color: var(--magenta);
  }

  /* Back */
  .card--back {
    background: var(--paper);
  }
  .back-wordmark {
    position: absolute;
    left: 52px;
    top: 70px;
    font-size: 48px;
    font-weight: 500;
    letter-spacing: 1px;
    color: var(--magenta);
  }
  .contact {
    position: absolute;
    left: 58px;
    top: 176px;
    color: var(--text-dark);
  }
  .contact-name {
    font-size: 30px;
    font-weight: 700;
    background: linear-gradient(90deg, var(--magenta) 0%, var(--violet) 45%, var(--teal) 70%, var(--navy-ink) 100%);
    -webkit-background-clip: text;
    background-clip: text;
    color: transparent;
    line-height: 1.1;
  }
  .contact-role {
    font-size: 17px;
    margin-top: 4px;
  }
  .contact-address {
    font-size: 17px;
    line-height: 1.35;
    margin-top: 18px;
    margin-left: 16px;
  }
  .contact-lines {
    list-style: none;
    margin-top: 16px;
    margin-left: 28px;
    font-size: 17px;
    line-height: 1.45;
  }
  .contact-lines li {
    display: flex;
    align-items: center;
    gap: 8px;
  }
  .contact-lines svg { width: 15px; height: 15px; flex: none; }
  .back-symbol-area {
    position: absolute;
    right: 40px;
    top: 40px;
    width: 240px;
    height: 320px;
    border-radius: 60px;
    background: linear-gradient(160deg, var(--navy-ink) 0%, var(--violet) 50%, var(--teal) 100%);
    opacity: 0.85;
  }
</style>
</head>
<body>
  <main class="sheet">
    <section class="card card--front">
      <div class="front-texture" role="img" aria-label="Subtle embossed brand pattern on dark navy"></div>
      <div class="front-wordmark">Veltrano</div>
    </section>

    <section class="card card--back">
      <div class="back-wordmark">Veltrano</div>

      <div class="contact">
        <h1 class="contact-name">Mathis CORLAVE</h1>
        <p class="contact-role">Co-Founder &amp; CEO</p>
        <p class="contact-address">17 rue des Tanneurs<br>69002 LYON</p>
        <ul class="contact-lines">
          <li>
            <svg viewBox="0 0 16 16" aria-hidden="true"><path d="M3 1.5l2.5 0 1 3.5-1.6 1.2a8 8 0 0 0 4.9 4.9l1.2-1.6 3.5 1v2.5a1.5 1.5 0 0 1-1.6 1.5A13 13 0 0 1 1.5 3.1 1.5 1.5 0 0 1 3 1.5z" fill="#e0189a"/></svg>
            (+33) 6 58 24 90 37
          </li>
          <li>
            <svg viewBox="0 0 16 16" aria-hidden="true"><rect x="1" y="3" width="14" height="10" rx="1" fill="#8a3fb0"/><path d="M1.5 3.5L8 9l6.5-5.5" stroke="#fff" stroke-width="1.3" fill="none"/></svg>
            mathis@veltrano.io
          </li>
          <li>
            <svg viewBox="0 0 16 16" aria-hidden="true"><circle cx="8" cy="8" r="6.5" fill="none" stroke="#0a6f9a" stroke-width="1.4"/><ellipse cx="8" cy="8" rx="2.8" ry="6.5" fill="none" stroke="#0a6f9a" stroke-width="1.2"/><path d="M1.5 8h13" stroke="#0a6f9a" stroke-width="1.2"/></svg>
            www.veltrano.io
          </li>
        </ul>
      </div>

      <div class="back-symbol-area" role="img" aria-label="Large brand symbol decoration in navy, magenta and teal gradient"></div>
    </section>
  </main>
</body>
</html>
```